Working Capital graphics

Our business advisory firm requires 9 images to be re-created and improved in the branding of our business.

The 9 images have been uploaded below and the colours and branding of the business can be found at the website www.thornwickadvisory.com.au

```html
<!DOCTYPE html>
<html lang="en">
<head>
<meta charset="utf-8">
<title>Working Capital Cycle</title>
<link rel="stylesheet" href="https://fonts.googleapis.com/css2?family=Source+Sans+3:wght@600;700&family=Lora:wght@700&display=swap">
<style>
  :root {
    --ink: #0f2a44;
    --teal: #1b8a8f;
    --teal-soft: #e9f4f4;
    --gold: #c8962e;
    --gold-deep: #a87a1f;
    --navy: #16365a;
    --white: #ffffff;
  }
  html, body {
    margin: 0;
    padding: 0;
    width: 1200px;
    height: 1200px;
    overflow: hidden;
    background: var(--white);
  }
  .cycle-diagram { display: block; width: 1200px; height: 1200px; }
  .step {
    font-family: "Source Sans 3", Arial, sans-serif;
    font-weight: 600;
    font-size: 25px;
    fill: var(--ink);
    text-anchor: middle;
  }
  .cycle-ring { fill: var(--teal-soft); }
  .cycle-title {
    font-family: "Lora", Georgia, serif;
    font-weight: 700;
    font-size: 36px;
    fill: var(--gold-deep);
    text-anchor: middle;
  }
  .flow-arrow { stroke: var(--teal); stroke-width: 4; stroke-linecap: round; fill: none; }
  .hub-arrow { stroke-width: 4.5; stroke-linecap: round; fill: none; }
  .hub-arrow-ar { stroke: var(--gold); }
  .hub-arrow-inv { stroke: var(--teal); }
  .hub-arrow-ap { stroke: var(--navy); }
  .cycle-tag rect { fill: var(--ink); }
  .cycle-tag text {
    font-family: "Source Sans 3", Arial, sans-serif;
    font-weight: 700;
    font-size: 25px;
    letter-spacing: 0.5px;
    fill: var(--white);
    text-anchor: middle;
  }
  .hub-ar { fill: var(--gold); }
  .hub-inv { fill: var(--teal); }
  .hub-ap { fill: var(--navy); }
  .hub-divider { stroke: var(--white); stroke-width: 2; }
  .hub-label {
    font-family: "Source Sans 3", Arial, sans-serif;
    font-weight: 700;
    font-size: 24px;
    fill: var(--white);
    text-anchor: middle;
  }
</style>
</head>
<body>
<svg class="cycle-diagram" viewBox="0 0 1500 1500" xmlns="http://www.w3.org/2000/svg" role="img" aria-label="Working capital cycle: revenue, supply chain and expenditure management">
  <defs>
    <marker id="head-teal" viewBox="0 0 10 10" refX="6" refY="5" markerWidth="4" markerHeight="4" orient="auto">
      <path d="M0,0 L10,5 L0,10 z" fill="#1b8a8f"/>
    </marker>
    <marker id="head-gold" viewBox="0 0 10 10" refX="6" refY="5" markerWidth="4" markerHeight="4" orient="auto">
      <path d="M0,0 L10,5 L0,10 z" fill="#c8962e"/>
    </marker>
    <marker id="head-navy" viewBox="0 0 10 10" refX="6" refY="5" markerWidth="4" markerHeight="4" orient="auto">
      <path d="M0,0 L10,5 L0,10 z" fill="#16365a"/>
    </marker>
  </defs>

  <!-- Revenue management -->
  <g class="cycle cycle-revenue">
    <circle class="cycle-ring" cx="398" cy="430" r="160"/>
    <text class="cycle-title" x="398" y="416">Revenue<tspan x="398" dy="38">Management</tspan></text>
    <text class="step" x="404" y="221">Customer<tspan x="404" dy="30">Strategy</tspan></text>
    <text class="step" x="580" y="238">Sales<tspan x="580" dy="30">Management</tspan></text>
    <text class="step" x="602" y="308">Risk<tspan x="602" dy="30">Management</tspan></text>
    <text class="step" x="660" y="395">Contract<tspan x="660" dy="30">Management</tspan></text>
    <text class="step" x="652" y="490">Sales Order<tspan x="652" dy="30">Processing</tspan></text>
    <text class="step" x="560" y="591">Credit<tspan x="560" dy="30">Check</tspan></text>
    <text class="step" x="424" y="616">Order<tspan x="424" dy="30">Fulfillment</tspan></text>
    <text class="step" x="277" y="616">Billing</text>
    <text class="step" x="195" y="544">Customer<tspan x="195" dy="30">Service</tspan></text>
    <text class="step" x="159" y="437">Cash<tspan x="159" dy="30">Collection</tspan></text>
    <text class="step" x="182" y="333">Receipt &amp;<tspan x="182" dy="30">Allocation</tspan><tspan x="182" dy="30">of Cash</tspan></text>
    <text class="step" x="240" y="251">Cash<tspan x="240" dy="30">Management</tspan></text>
    <g marker-end="url(#head-teal)">
      <line class="flow-arrow" x1="318" y1="252" x2="346" y2="241"/>
      <line class="flow-arrow" x1="466" y1="240" x2="494" y2="252"/>
      <line class="flow-arrow" x1="533" y1="275" x2="555" y2="296"/>
      <line class="flow-arrow" x1="594" y1="357" x2="601" y2="384"/>
      <line class="flow-arrow" x1="609" y1="430" x2="606" y2="458"/>
      <line class="flow-arrow" x1="586" y1="528" x2="572" y2="553"/>
      <line class="flow-arrow" x1="520" y1="601" x2="494" y2="616"/>
      <line class="flow-arrow" x1="350" y1="628" x2="322" y2="616"/>
      <line class="flow-arrow" x1="283" y1="591" x2="261" y2="572"/>
      <line class="flow-arrow" x1="220" y1="512" x2="211" y2="484"/>
      <line class="flow-arrow" x1="207" y1="440" x2="207" y2="409"/>
      <line class="flow-arrow" x1="240" y1="320" x2="262" y2="296"/>
    </g>
    <g class="cycle-tag">
      <rect x="273" y="663" width="263" height="45" rx="22.5"/>
      <text x="404" y="694">Customer to Cash</text>
    </g>
  </g>

  <!-- Supply chain management -->
  <g class="cycle cycle-supply">
    <circle class="cycle-ring" cx="1108" cy="430" r="150"/>
    <text class="cycle-title" x="1108" y="416">Supply Chain<tspan x="1108" dy="38">Management</tspan></text>
    <text class="step" x="1094" y="213">Supply<tspan x="1094" dy="30">chain</tspan><tspan x="1094" dy="30">strategy</tspan></text>
    <text class="step" x="1269" y="277">Product Range<tspan x="1269" dy="30">Management</tspan></text>
    <text class="step" x="1333" y="369">Forecasting</text>
    <text class="step" x="1336" y="435">Sales Order<tspan x="1336" dy="30">Forecasting</tspan></text>
    <text class="step" x="1285" y="537">Production<tspan x="1285" dy="30">Scheduling</tspan></text>
    <text class="step" x="1104" y="604">Raw Material<tspan x="1104" dy="30">Planning</tspan></text>
    <text class="step" x="934" y="537">Production<tspan x="934" dy="30">Planning</tspan></text>
    <text class="step" x="854" y="451">Production</text>
    <text class="step" x="864" y="369">Warehousing</text>
    <text class="step" x="945" y="291">Distribution</text>
    <g marker-end="url(#head-teal)">
      <line class="flow-arrow" x1="1005" y1="258" x2="1036" y2="245"/>
      <line class="flow-arrow" x1="1146" y1="242" x2="1176" y2="253"/>
      <line class="flow-arrow" x1="1253" y1="313" x2="1270" y2="337"/>
      <line class="flow-arrow" x1="1288" y1="378" x2="1293" y2="406"/>
      <line class="flow-arrow" x1="1288" y1="476" x2="1279" y2="503"/>
      <line class="flow-arrow" x1="1226" y1="578" x2="1202" y2="596"/>
      <line class="flow-arrow" x1="1018" y1="608" x2="992" y2="595"/>
      <line class="flow-arrow" x1="917" y1="500" x2="909" y2="472"/>
      <line class="flow-arrow" x1="904" y1="420" x2="909" y2="390"/>
      <line class="flow-arrow" x1="924" y1="338" x2="942" y2="315"/>
    </g>
    <g class="cycle-tag">
      <rect x="947" y="664" width="314" height="44" rx="22"/>
      <text x="1104" y="694">Forecast to Fulfillment</text>
    </g>
  </g>

  <!-- Working capital hub -->
  <g class="hub">
    <polygon class="hub-ar" points="782,567 588,761 782,683"/>
    <polygon class="hub-inv" points="782,567 977,761 782,683"/>
    <polygon class="hub-ap" points="588,761 977,761 782,683"/>
    <line class="hub-divider" x1="782" y1="567" x2="782" y2="683"/>
    <line class="hub-divider" x1="782" y1="683" x2="588" y2="761"/>
    <line class="hub-divider" x1="782" y1="683" x2="977" y2="761"/>
    <text class="hub-label" transform="translate(726,670) rotate(-45)">A/R</text>
    <text class="hub-label" transform="translate(836,663) rotate(45)">Inventory</text>
    <text class="hub-label" x="782" y="735">A/P</text>
    <line class="hub-arrow hub-arrow-ar" x1="682" y1="645" x2="658" y2="621" marker-end="url(#head-gold)"/>
    <line class="hub-arrow hub-arrow-inv" x1="890" y1="643" x2="915" y2="619" marker-end="url(#head-teal)"/>
    <line class="hub-arrow hub-arrow-ap" x1="789" y1="780" x2="789" y2="814" marker-end="url(#head-navy)"/>
  </g>

  <!-- Expenditure management -->
  <g class="cycle cycle-expenditure">
    <circle class="cycle-ring" cx="775" cy="1048" r="150"/>
    <text class="cycle-title" x="775" y="1034">Expenditure<tspan x="775" dy="38">Management</tspan></text>
    <text class="step" x="770" y="863">Purchasing<tspan x="770" dy="30">Strategy</tspan></text>
    <text class="step" x="951" y="909">Budgeting &amp;<tspan x="951" dy="30">Forecasting</tspan></text>
    <text class="step" x="1029" y="991">Originating<tspan x="1029" dy="30">Requirements</tspan></text>
    <text class="step" x="1021" y="1093">Selecting &amp;<tspan x="1021" dy="30">Negotiating</tspan></text>
    <text class="step" x="956" y="1176">Ordering &amp;<tspan x="956" dy="30">Contracting</tspan></text>
    <text class="step" x="779" y="1222">Receiving &amp;<tspan x="779" dy="30">Evaluating</tspan></text>
    <text class="step" x="611" y="1176">Discrepancy<tspan x="611" dy="30">Management</tspan></text>
    <text class="step" x="540" y="1086">Invoice<tspan x="540" dy="30">Processing</tspan></text>
    <text class="step" x="528" y="998">Payment<tspan x="528" dy="30">Issuance</tspan></text>
    <text class="step" x="611" y="901">Cash<tspan x="611" dy="30">Management</tspan></text>
    <g marker-end="url(#head-teal)">
      <line class="flow-arrow" x1="664" y1="883" x2="692" y2="868"/>
      <line class="flow-arrow" x1="851" y1="870" x2="878" y2="885"/>
      <line class="flow-arrow" x1="940" y1="955" x2="951" y2="983"/>
      <line class="flow-arrow" x1="964" y1="1035" x2="964" y2="1063"/>
      <line class="flow-arrow" x1="946" y1="1123" x2="932" y2="1149"/>
      <line class="flow-arrow" x1="886" y1="1208" x2="860" y2="1220"/>
      <line class="flow-arrow" x1="704" y1="1225" x2="678" y2="1212"/>
      <line class="flow-arrow" x1="615" y1="1155" x2="602" y2="1131"/>
      <line class="flow-arrow" x1="580" y1="1065" x2="581" y2="1037"/>
      <line class="flow-arrow" x1="590" y1="978" x2="603" y2="953"/>
    </g>
    <g class="cycle-tag">
      <rect x="603" y="1281" width="333" height="47" rx="23.5"/>
      <text x="770" y="1313">Purchase to Pay</text>
    </g>
  </g>
</svg>
</body>
</html>
```